Amber Tides: Lantern Tales from Seven Winters by the Northern Sea and Other Small Wonders

Good day! I am excited to work again with you, amazing designers! This time I am looking for the cover design of my book.
Dimensions 6” x 9”
The book name is as my name project. I love simplicity, but yet that is impactful. I love colours, I don't have a specific colour in mind, but I like the mustard colour as the one in the logo of my company. I am open to ideas! I have attached some cover samples that I like so that it gives a better idea of what I have on mind.
I am looking for something that looks professional, yet, not super serious, that it's approachable to people. Something that calls their attention at first glance.
I am working with my editor and my interior designer as well to finalize this part of the book. I will be working with the person that I select for the book design to finalize it.
About the book, here a passage of an unedited version of the introduction for guidance :
My intention is to take you on a journey to help you to understand what is going on in your mind so that you get out from anything that is holding you back in your life. My intention is to guide you to start fully living and experiencing a life that your mind even have yet conceived. To experience a life where you live fearless and without suffering. Living your life where you are the navigator and the creator of how you are experiencing it and you are living in a world of possibilities where there are no limitations.
For it, we will start to understand more about the mind and about the brain. I am not a neuroscientist and neither I consider my self an expert in the workings of the brain, what I know is the result of my fascination about our brain. This curiosity and the part of me that likes to understand how things work took me to read, research and learn about how our brain works and how its intrinsic mechanisms are subconsciously influencing and limiting us. I encourage you to stay on this part, it can be a bit technical, but understanding how it works will empower you not to allow your mind to dictate the way you approach your life and to live on autopilot.
We will continue to describe how you have been programmed throughout your life, putting you inside a box limited by your subconscious beliefs and ideas about the world. In this part, we will also discuss what ego is, how it is subconsciously limiting you and how the ways of when ego manifests itself are limiting you and making you suffer. Now that you know how you have been enclosed in your mind for all your life, we will move to discuss how you can get out of it. You will learn how to master your emotions to eliminate your suffering and not allow them to control the direction of your life and use them as a mechanism to get out from your programed mind. We continue to discuss how to leverage the power of your mind and harness your power of choice. Finally, I invite you to see yourself as a holistic being so that you start truly living and take control over the direction of your life, by nourishing and taking care of all those aspects of you utilizing their wisdom and synergy to achieve higher connection within yourself, your soul and live your life in a higher level of consciousness with peace, flow, love and purpose.

```html
<!DOCTYPE html>
<html lang="en">
<head>
<meta charset="utf-8">
<title>Amber Tides – Book Cover</title>
<link href="https://fonts.googleapis.com/css2?family=Anton&family=Jost:wght@400;500&display=swap" rel="stylesheet">
<style>
  :root {
    --stage: #464646;
    --title-blue: #0a74c4;
    --subtitle-ink: #1d1d1f;
    --author-navy: #1d3f8c;
    --mustard-warm: #c9a866;
    --frame-tan: #cdbba3;
    --light-cream: #f3efe9;
    --sky-pale: #e4eef3;
    --shirt-blue: #c3d7e6;
    --linen-white: #f7f6f3;
  }
  * { margin: 0; padding: 0; box-sizing: border-box; }
  html, body {
    width: 1200px;
    height: 800px;
    overflow: hidden;
    background: var(--stage);
  }
  .stage {
    position: relative;
    width: 1200px;
    height: 800px;
    display: flex;
    align-items: center;
    justify-content: center;
  }
  .cover {
    position: relative;
    width: 480px;
    height: 720px;
    overflow: hidden;
  }
  .cover-photo {
    position: absolute;
    inset: 0;
    display: block;
  }
  .cover-title {
    position: absolute;
    top: 320px;
    left: 0;
    right: 0;
    text-align: center;
    font-family: "Anton", "Impact", sans-serif;
    font-weight: 400;
    font-size: 84px;
    line-height: 1;
    color: var(--title-blue);
    text-transform: uppercase;
    white-space: nowrap;
  }
  .cover-subtitle {
    position: absolute;
    top: 424px;
    left: 52px;
    right: 52px;
    text-align: center;
    font-family: "Jost", "Futura", sans-serif;
    font-weight: 400;
    font-size: 19px;
    line-height: 1.3;
    color: var(--subtitle-ink);
    text-transform: uppercase;
  }
  .cover-author {
    position: absolute;
    top: 636px;
    left: 0;
    right: 0;
    text-align: center;
    font-family: "Jost", "Futura", sans-serif;
    font-weight: 400;
    font-size: 28px;
    letter-spacing: 0.18em;
    color: var(--author-navy);
    text-transform: uppercase;
    white-space: nowrap;
  }
</style>
</head>
<body>
  <main class="stage">
    <article class="cover">
      <svg class="cover-photo" width="480" height="720" viewBox="0 0 480 720"
           role="img" aria-label="Photograph of a woman seen from behind in a pale blue shirt, opening white French doors onto a bright morning, an unmade white bed in the foreground">
        <defs>
          <linearGradient id="room-light" x1="0" y1="0" x2="1" y2="0">
            <stop offset="0" stop-color="var(--mustard-warm)"/>
            <stop offset="0.1" stop-color="var(--frame-tan)"/>
            <stop offset="0.28" stop-color="var(--light-cream)"/>
            <stop offset="0.5" stop-color="var(--sky-pale)"/>
            <stop offset="0.72" stop-color="var(--light-cream)"/>
            <stop offset="0.9" stop-color="var(--frame-tan)"/>
            <stop offset="1" stop-color="var(--mustard-warm)"/>
          </linearGradient>
          <radialGradient id="figure-glow" cx="0.5" cy="0.55" r="0.5">
            <stop offset="0" stop-color="var(--shirt-blue)" stop-opacity="0.85"/>
            <stop offset="1" stop-color="var(--shirt-blue)" stop-opacity="0"/>
          </radialGradient>
          <linearGradient id="top-shade" x1="0" y1="0" x2="0" y2="1">
            <stop offset="0" stop-color="var(--frame-tan)" stop-opacity="0.7"/>
            <stop offset="1" stop-color="var(--frame-tan)" stop-opacity="0"/>
          </linearGradient>
          <linearGradient id="bed-linen" x1="0" y1="0" x2="0" y2="1">
            <stop offset="0" stop-color="var(--linen-white)" stop-opacity="0"/>
            <stop offset="0.6" stop-color="var(--linen-white)" stop-opacity="0.95"/>
            <stop offset="1" stop-color="#e9e4dc"/>
          </linearGradient>
        </defs>
        <rect width="480" height="720" fill="url(#room-light)"/>
        <rect width="480" height="80" fill="url(#top-shade)"/>
        <ellipse cx="240" cy="420" rx="150" ry="260" fill="url(#figure-glow)"/>
        <rect y="560" width="480" height="160" fill="url(#bed-linen)"/>
      </svg>

      <h1 class="cover-title">Amber Tides</h1>
      <p class="cover-subtitle">Lantern Tales from Seven Winters by the Northern Sea and Other Small Wonders</p>
      <p class="cover-author">Author Name</p>
    </article>
  </main>
</body>
</html>
```